Hearing Pal

Conference flyer. Target audience is for attorneys and bail agents. App allows their clients to check-in, make payments and receive payments.
See website hearingpalapp.com for product
Details. Emphasize Payment button, check-ins and court reminders.

Target Market(s)

Attorneys, Bail Agents, courts, probation

Industry/Entity Type

Court House

Requirements
Nice to have
• Picture of someone taking a selfie for a check-in!

```html
<!DOCTYPE html>
<html lang="en">
<head>
<meta charset="utf-8">
<title>Hearing Pal – Conference Flyer</title>
<link rel="stylesheet" href="https://fonts.googleapis.com/css2?family=Gelasio:wght@400;700&family=Open+Sans:wght@400;600&display=swap">
<style>
  :root {
    --stage: #a9a9a9;
    --paper: #ffffff;
    --paper-soft: #eef0f3;
    --navy: #0f3b8c;
    --navy-deep: #12306e;
    --ink: #111111;
    --ink-soft: #2a2a2a;
    --band: #050505;
    --white: #ffffff;
  }
  * { box-sizing: border-box; margin: 0; padding: 0; }
  html, body { width: 900px; height: 1200px; overflow: hidden; }
  body {
    background: var(--stage);
    position: relative;
    font-family: "Open Sans", Arial, sans-serif;
    color: var(--ink);
  }
  .flyer {
    position: absolute; left: 100px; top: 90px;
    width: 700px; height: 990px;
    background: var(--paper);
    overflow: hidden;
    box-shadow: 0 2px 10px rgba(0,0,0,.25);
  }
  .flyer > * { position: absolute; }

  .hero-photo {
    left: 0; top: 0; width: 355px; height: 355px;
    background: linear-gradient(90deg, #c9ccd3 0%, #d9dbe0 45%, #e9ebee 80%, #ffffff 100%);
  }
  .hero-photo::after {
    content: ""; position: absolute; left: 110px; top: 60px; width: 150px; height: 295px;
    background: linear-gradient(180deg, #e7809a 0%, #d96c86 60%, #4a4a4a 100%);
    opacity: .55; border-radius: 60px 60px 0 0;
  }

  .brand-mark {
    left: 455px; top: 35px; width: 145px; height: 145px;
    display: flex; align-items: center; justify-content: center; flex-direction: column;
  }
  .brand-mark .dot {
    width: 26px; height: 26px; border-radius: 50%; background: var(--navy); margin-bottom: 8px;
  }
  .brand-mark .name {
    font-family: "Gelasio", Georgia, serif; font-weight: 700; font-size: 22px; color: var(--navy);
    white-space: nowrap;
  }

  .hero-copy { left: 360px; top: 180px; width: 320px; text-align: center; }
  .hero-kicker { font-family: "Gelasio", Georgia, serif; font-size: 19px; letter-spacing: .3px; color: var(--ink-soft); }
  .hero-title { font-family: "Gelasio", Georgia, serif; font-weight: 700; font-size: 34px; line-height: 1.05; margin-top: 4px; color: var(--ink); }
  .hero-title .accent { display: block; font-weight: 400; font-size: 30px; color: var(--navy); margin-top: 2px; }
  .hero-text { font-size: 12px; font-weight: 600; line-height: 1.3; margin: 14px auto 0; width: 280px; color: var(--ink); }

  .band { left: 0; top: 380px; width: 700px; height: 187px; background: var(--band); }
  .band-feature {
    left: 0; top: 400px; width: 355px; height: 167px; background: var(--navy);
    padding: 20px 14px 0 35px; color: var(--white);
  }
  .band-feature h2 { font-family: "Gelasio", Georgia, serif; font-weight: 700; font-size: 21px; line-height: 1.25; }
  .band-feature p { font-size: 10.5px; line-height: 1.45; margin-top: 6px; }
  .band-claim {
    left: 360px; top: 428px; width: 340px; text-align: center; color: var(--white);
    font-family: "Gelasio", Georgia, serif;
  }
  .band-claim p { font-size: 21px; line-height: 1.35; }
  .band-claim strong { display: block; font-size: 38px; font-weight: 700; line-height: 1.2; margin-top: 2px; }
  .band-claim strong span { font-family: "Open Sans", Arial, sans-serif; }

  .lower { left: 0; top: 567px; width: 700px; height: 360px;
    background: linear-gradient(90deg, var(--paper) 0%, var(--paper) 55%, var(--paper-soft) 100%); }

  .phone-photo {
    left: 415px; top: 545px; width: 285px; height: 405px;
    background: linear-gradient(160deg, #3d4048 0%, #5f86cf 35%, #4f7ccf 65%, #e8c2a8 100%);
    border-radius: 40px 0 0 0;
  }

  .pillars { left: 30px; top: 625px; width: 370px; }
  .pillar { position: relative; padding-left: 44px; margin-bottom: 16px; }
  .pillar-icon {
    position: absolute; left: 0; top: 0; width: 36px; height: 36px;
  }
  .pillar h3 { font-family: "Gelasio", Georgia, serif; font-size: 25px; font-weight: 700; color: #222; line-height: 36px; }
  .pillar h3 .accent { color: var(--navy); }
  .pillar p { font-size: 15px; line-height: 1.3; margin-left: -42px; color: var(--ink-soft); }

  .footer-dark {
    left: 0; top: 927px; width: 440px; height: 63px; background: var(--band);
    clip-path: polygon(0 0, 420px 0, 440px 100%, 0 100%);
  }
  .footer-blue {
    left: 295px; top: 950px; width: 405px; height: 40px; background: var(--navy-deep);
    clip-path: polygon(12px 0, 100% 0, 100% 100%, 0 100%);
  }
  .footer-phone { left: 64px; top: 942px; font-family: "Gelasio", Georgia, serif; font-size: 19px; color: var(--white); }
  .footer-web { left: 390px; top: 962px; font-family: "Gelasio", Georgia, serif; font-size: 14px; letter-spacing: 2.5px; color: var(--white); }
</style>
</head>
<body>
  <main class="flyer">
    <div class="hero-photo" role="img" aria-label="Photo of a woman in glasses and a pink blouse taking a check-in selfie in an office"></div>

    <div class="brand-mark">
      <span class="dot"></span>
      <span class="name">Hearing Pal</span>
    </div>

    <header class="hero-copy">
      <p class="hero-kicker">EMPHASIZE PAYMENT BUTTON</p>
      <h1 class="hero-title">CHECK-INS AND <span class="accent">COURT REMINDERS</span></h1>
      <p class="hero-text">Simply open your Hearing Pal App and check-in with a Selfie or record a video. available on IOS or Android</p>
    </header>

    <div class="band"></div>
    <section class="band-feature">
      <h2>Check-in as easy as taking a Selfie!</h2>
      <p>hearing pal app helps guide you through your day in court from the arrest date until trial and any probation period. hearing pal app allows you to keep in constant contact with your court and all your court providers in one app.</p>
    </section>
    <div class="band-claim">
      <p>our team as been working with<br>law enforcement and the courts</p>
      <strong>FOR <span>40</span> YEARS</strong>
    </div>

    <div class="lower"></div>
    <div class="phone-photo" role="img" aria-label="Photo of a hand holding a smartphone showing the client app screen with contact and payment buttons"></div>

    <section class="pillars">
      <div class="pillar">
        <svg class="pillar-icon" viewBox="0 0 36 36" aria-hidden="true">
          <circle cx="18" cy="18" r="16.5" fill="none" stroke="#12306e" stroke-width="2"/>
          <rect x="11" y="9" width="14" height="18" rx="1.5" fill="none" stroke="#12306e" stroke-width="1.8"/>
          <path d="M14 14h8M14 18h8M14 22h5" stroke="#12306e" stroke-width="1.6"/>
        </svg>
        <h3><span class="accent">WHO</span> Are We</h3>
        <p>our team is made up of court providers and developers.</p>
      </div>
      <div class="pillar">
        <svg class="pillar-icon" viewBox="0 0 36 36" aria-hidden="true">
          <circle cx="18" cy="18" r="16.5" fill="none" stroke="#12306e" stroke-width="2"/>
          <path d="M8 18l5-5 5 3 5-3 5 5-7 6-3-2-3 2z" fill="#12306e"/>
        </svg>
        <h3><span class="accent">OUR</span> Mission</h3>
        <p>it is our mission to help our clients navigate the fast paced and sometimes confusing court system.</p>
      </div>
      <div class="pillar">
        <svg class="pillar-icon" viewBox="0 0 36 36" aria-hidden="true">
          <circle cx="18" cy="18" r="16.5" fill="none" stroke="#12306e" stroke-width="2"/>
          <path d="M16 27v-15a2 2 0 0 1 4 0v7l4 1a2 2 0 0 1 2 2v5z" fill="none" stroke="#12306e" stroke-width="1.8" stroke-linejoin="round"/>
          <circle cx="18" cy="11" r="4.5" fill="none" stroke="#12306e" stroke-width="1.2"/>
        </svg>
        <h3><span class="accent">WHAT</span> We Do</h3>
        <p>we help our clients stay in touch with the courts and the court providers.</p>
      </div>
    </section>

    <div class="footer-dark"></div>
    <div class="footer-blue"></div>
    <p class="footer-phone">+1 555-014-2870</p>
    <p class="footer-web">www.hearingpalapp.com</p>
  </main>
</body>
</html>
```